Brevane Mobile Nutrition Funnel Pouch & Cap Pouch

The Funnel Pouch (without cap), Funnel Pouch (with cap), and Box will be using the same design and style, expect a few small changes for each.

Funnel Pouch (one time use)
1. Design for front and back of a Funnel Pouch & With Cap Funnel Pouch
2. Attached are the design requirements and photo of products

Funnel Pouch (Reusable)
3. this is the product WITH cap
4. the only difference in this design is that
"Spin n' Seal Cap" and "Reusable" need to be added somewhere on fron and back
- but overall it is the same design as the funnel pouch with no cap

After design is completed,
5. Professional white background image of both Funnel pouches

I have attached some examples of other products where you can get some ideas.
Updates

I am looking for a professional designer who I plan to work with long term for multiple projects. Please submit soon, thanks! Added Friday, April 7, 2017

Target Market(s)

health/ fitness enthusiasts, outdoor market, on the go indivudals, gym goers, Tallow Sports and Outdoors, Fernbrook Grocers

Industry/Entity Type

Supplement

Requirements
Must have
• Professional, creative design that follows basic requirements.
Nice to have
• incorporate BREVANE because that is our company logo name.
Should not have
• Should not be a design that I can easily make myself.

```html
<!DOCTYPE html>
<html lang="en">
<head>
<meta charset="utf-8">
<title>Brevane Mobile Nutrition – Funnel Pouch</title>
<link rel="stylesheet" href="https://fonts.googleapis.com/css2?family=Lato:wght@400;700;900&display=swap">
<style>
  :root {
    --stage: #f1f1f2;
    --pouch-white: #f4f4f7;
    --navy: #24308f;
    --navy-deep: #1c2680;
    --lavender: #9c9fd8;
    --lavender-soft: #c9cbec;
    --mist: #e3e4f4;
    --signal-red: #e2392a;
    --signal-red-soft: #ee6b57;
    --cap: #f7f8f9;
    --cap-edge: #d6d9dd;
    --ink-white: #ffffff;
  }
  html, body {
    margin: 0;
    padding: 0;
    width: 899px;
    height: 1200px;
    overflow: hidden;
    background: var(--stage);
  }
  .canvas {
    position: relative;
    width: 899px;
    height: 1200px;
    font-family: "Lato", Arial, sans-serif;
  }
  .pouch-art {
    position: absolute;
    left: 0;
    top: 0;
  }
  .brand-name {
    position: absolute;
    left: 254px;
    width: 400px;
    top: 158px;
    text-align: center;
    font-weight: 400;
    font-size: 32px;
    line-height: 36px;
    letter-spacing: 3px;
    color: var(--navy);
  }
  .product-title {
    position: absolute;
    left: 253px;
    width: 400px;
    top: 214px;
    margin: 0;
    text-align: center;
    font-weight: 900;
    font-size: 51px;
    line-height: 50px;
    letter-spacing: 2px;
    color: var(--navy);
  }
  .step {
    position: absolute;
    text-align: center;
    width: 170px;
  }
  .step-number {
    display: block;
    font-weight: 900;
    font-size: 42px;
    line-height: 44px;
  }
  .step-verb {
    display: block;
    font-weight: 900;
    font-size: 21px;
    letter-spacing: 3px;
    line-height: 26px;
  }
  .step-note {
    display: block;
    font-weight: 700;
    font-size: 17px;
    line-height: 23px;
  }
  .step-load {
    left: 300px;
    top: 344px;
    color: var(--navy);
  }
  .step-dispense {
    left: 302px;
    top: 560px;
    color: var(--ink-white);
  }
  .step-dispense .step-verb { color: var(--mist); }
</style>
</head>
<body>
<main class="canvas">
  <svg class="pouch-art" width="899" height="1200" viewBox="0 0 899 1200">
    <defs>
      <clipPath id="pouch-face">
        <path d="M192,68 L688,70 L576,992 L328,992 Z"/>
      </clipPath>
      <linearGradient id="usage-fill" x1="0" y1="0" x2="0" y2="1">
        <stop offset="0" stop-color="var(--signal-red)"/>
        <stop offset="1" stop-color="var(--signal-red-soft)"/>
      </linearGradient>
    </defs>

    <g class="spout-cap">
      <rect x="392" y="984" width="104" height="44" rx="4" fill="var(--cap)" stroke="var(--cap-edge)" stroke-width="2"/>
      <rect x="388" y="1026" width="112" height="142" rx="8" fill="var(--cap)" stroke="var(--cap-edge)" stroke-width="2"/>
    </g>

    <g class="pouch-face" clip-path="url(#pouch-face)">
      <rect x="180" y="60" width="520" height="940" fill="var(--pouch-white)"/>
      <path class="band-left-outer" d="M180,60 L226,60 C250,300 330,450 470,720 L470,1000 L180,1000 Z" fill="var(--navy)"/>
      <path class="band-left-lavender" d="M226,60 L262,60 C290,300 380,470 500,720 L470,720 C330,450 250,300 226,60 Z" fill="var(--lavender)"/>
      <path class="band-left-soft" d="M262,60 L298,60 C330,300 420,470 530,730 L500,720 C380,470 290,300 262,60 Z" fill="var(--lavender-soft)"/>
      <path class="band-left-navy-inner" d="M300,380 C360,520 420,640 460,760 L470,1000 L430,1000 C420,800 380,620 300,380 Z" fill="var(--navy-deep)" opacity="0.55"/>
      <path class="band-left-lower" d="M470,720 L530,730 C545,820 548,900 540,1000 L470,1000 Z" fill="var(--lavender)"/>
      <path class="band-right-outer" d="M660,60 L700,60 L700,1000 L570,1000 C600,700 640,350 660,60 Z" fill="var(--navy)"/>
      <path class="band-right-lavender" d="M636,60 L660,60 C640,350 600,700 570,1000 L552,1000 C580,700 620,350 636,60 Z" fill="var(--lavender-soft)"/>
    </g>
    <path d="M192,68 L688,70 L576,992 L328,992 Z" fill="none" stroke="var(--navy-deep)" stroke-width="1.5"/>

    <rect class="usage-illustration" x="462" y="330" width="90" height="602" rx="10"
          fill="url(#usage-fill)" role="img"
          aria-label="Red illustration: a scoop pouring powder into a funnel, a drop falling into a sports bottle"/>
  </svg>

  <div class="brand-name">BREVANE</div>

  <h1 class="product-title">PORTABLE<br>NUTRITION</h1>

  <div class="step step-load">
    <span class="step-number">1</span>
    <span class="step-verb">LOAD</span>
    <span class="step-note">your mix</span>
  </div>

  <div class="step step-dispense">
    <span class="step-number">2</span>
    <span class="step-verb">DISPENSE</span>
    <span class="step-note">anytime<br>into any bottle</span>
  </div>
</main>
</body>
</html>
```